Hotel Business Card Project

Amber Crest Hotel will be a premium boutique hotel in Dhaka, Bangladesh. The hotel will offer the finest amenities and facilities available on the market, and the cost per room investment will far exceed other 5-star hotels currently in the market.

As a result, we wanted the business card to reflect that premium/luxurious/upscale feel, and also be elegant and hospitable at the same time.

The name 'Amber Crest' is derived from the fact that Bangladesh has 6 distinct seasons (you can get more information online if required, or contact me about it). The leaves in the logo has the tree because trees give people shade, protection and safety (just like our hotel would try to give).

Target Market(s)

Business professionals, guests

Industry/Entity Type

Investment

Requirements
Must have
• Elegant, Classy and very attractive business card.

Must be editable to enter specific Names, Positions, Phone numbers and email later on.
Nice to have
• The address would be: House 42, Road 57, Banani 4, Dhaka 1230, Bangladesh

Slogan- Luxury Redefined

```html
<!DOCTYPE html>
<html lang="en">
<head>
<meta charset="utf-8">
<title>Amber Crest Hotel — Business Card</title>
<link rel="stylesheet" href="https://fonts.googleapis.com/css2?family=Hind:wght@300;400;500&display=swap">
<style>
  :root {
    --crimson: #a42a32;
    --ink: #050505;
    --gold: #c9a45c;
    --gold-dark: #a87a3e;
    --gold-light: #f2e2ad;
    --gold-text: #9b6a32;
    --label-gold: #e0b24a;
    --paper: #ffffff;
    --stage: #e4e5e7;
  }
  * { margin: 0; padding: 0; box-sizing: border-box; }
  html, body { width: 1200px; height: 900px; overflow: hidden; }
  body {
    position: relative;
    background: radial-gradient(ellipse at center, #f4f4f5 0%, var(--stage) 100%);
    font-family: "Hind", sans-serif;
  }
  .card {
    position: absolute;
    left: 281px;
    width: 637px;
    height: 389px;
    background: var(--crimson);
    box-shadow: 3px 4px 6px rgba(0,0,0,0.35);
    overflow: hidden;
  }
  .card--front { top: 33px; }
  .card--back { top: 456px; }

  .gold-band {
    position: absolute;
    left: 0; width: 100%;
    background: linear-gradient(90deg, var(--gold-dark) 0%, #d9bc7c 22%, var(--gold-light) 50%, #d9bc7c 78%, var(--gold-dark) 100%);
    display: flex; flex-direction: column; align-items: center; justify-content: center;
    color: var(--gold-text);
  }
  .rule {
    position: absolute; left: 0; width: 100%; height: 1px;
    background: var(--gold);
  }

  .brand-seal {
    position: absolute;
    width: 196px; height: 196px;
    border-radius: 50%;
    background: var(--paper);
    border: 2px solid var(--gold);
    box-shadow: inset 0 0 0 5px var(--paper), inset 0 0 0 6px rgba(201,164,92,0.5);
    display: flex; align-items: center; justify-content: center;
    text-align: center;
  }
  .brand-seal__name {
    font-size: 24px; font-weight: 400; line-height: 1.05;
    color: #55575a; text-transform: uppercase; letter-spacing: 0.5px;
  }

  .card--front .brand-seal { left: 221px; top: 9px; }
  .card--front .rule--top { top: 244px; }
  .card--front .rule--bottom { top: 295px; }
  .slogan-band { top: 249px; height: 41px; }
  .slogan { font-size: 21px; font-weight: 400; letter-spacing: 0.8px; }

  .contact {
    position: absolute; left: 0; width: 100%; top: 328px;
    text-align: center; color: var(--paper);
  }
  .contact__address { font-size: 17px; font-weight: 300; letter-spacing: 0.4px; }
  .contact__lines { margin-top: 2px; font-size: 14px; font-weight: 300; }
  .contact__label { color: var(--label-gold); font-weight: 500; margin-left: 8px; }
  .contact__label:first-child { margin-left: 0; }

  .name-band { top: 45px; height: 78px; }
  .person-name { font-size: 24px; font-weight: 400; letter-spacing: 0.6px; line-height: 1; margin-top: 6px; }
  .person-role { font-size: 13px; font-weight: 400; letter-spacing: 3px; text-transform: uppercase; line-height: 1; margin-top: 3px; }

  .base-wave { position: absolute; left: 0; top: 0; width: 637px; height: 389px; }
  .card--back .brand-seal { left: 221px; top: 173px; }
</style>
</head>
<body>
  <section class="card card--front" aria-label="Card front">
    <div class="brand-seal">
      <span class="brand-seal__name">Amber Crest<br>Hotel</span>
    </div>
    <div class="rule rule--top"></div>
    <div class="gold-band slogan-band"><p class="slogan">Luxury Redefined</p></div>
    <div class="rule rule--bottom"></div>
    <div class="contact">
      <p class="contact__address">House 42, Road 57, Banani 4, Dhaka 1230, Bangladesh</p>
      <p class="contact__lines">
        <span class="contact__label">T:</span> 6790 214365
        <span class="contact__label">F:</span> 6790 563874
        <span class="contact__label">E:</span> ambercrest@hotel.com
        <span class="contact__label">W:</span> ambercresthotel.com
      </p>
    </div>
  </section>

  <section class="card card--back" aria-label="Card back">
    <div class="gold-band name-band">
      <p class="person-name">Rafiq Ahmed</p>
      <p class="person-role">Manager</p>
    </div>
    <svg class="base-wave" viewBox="0 0 637 389" aria-hidden="true">
      <path d="M0 245 Q318 160 637 245 L637 389 L0 389 Z" fill="var(--ink)"/>
      <path d="M0 235 Q318 150 637 235" fill="none" stroke="var(--gold)" stroke-width="1.5"/>
      <path d="M0 245 Q318 160 637 245" fill="none" stroke="var(--gold)" stroke-width="1.5"/>
    </svg>
    <div class="brand-seal">
      <span class="brand-seal__name">Amber Crest<br>Hotel</span>
    </div>
  </section>
</body>
</html>
```